Personalised nutrition and health DNA report redesign

As part of our DNA report redesign, we are looking for new colour scheme that fits around our brand colours, more professional and slick design and more visual content/less text, but that conveys the same messages. We want it to be more visually appealing to customers and more user friendly and intuitive. We would like to it appeal to both males and females. It would be preferred for it to be done in Adobe InDesign and to receive the source file. I would need all pages redesigned. Thank you!
Target Market(s)
Mostly females, 30-55 but also some younger and middle aged men, professionals interested in their health
Industry/Entity Type
Health tech, Wellness
Look and feel

```html
<!DOCTYPE html>
<html lang="en">
<head>
<meta charset="utf-8">
<title>nutrava wellness — DNA Report Pages</title>
<link href="https://fonts.googleapis.com/css2?family=Montserrat:wght@400;500;600;700;800&display=swap" rel="stylesheet">
<style>
:root{
  --stage:#262626;
  --blue:#1f6bf2;
  --blue-bright:#2e86ff;
  --blue-sky:#5cb6ff;
  --blue-pale:#9ec8ff;
  --ink:#111318;
  --muted:#3a3f4a;
  --page-top:#ffffff;
  --page-bottom:#8eaaf6;
  --magenta:#d316f0;
  --orange:#f06a12;
}
*{box-sizing:border-box;margin:0;padding:0}
html,body{width:1200px;height:686px;overflow:hidden;background:var(--stage)}
body{position:relative;font-family:"Montserrat",Arial,sans-serif;color:var(--ink)}
.page{position:absolute;width:206px;height:292px;overflow:hidden;
  background:linear-gradient(180deg,var(--page-top) 0%,var(--page-top) 60%,#d7e1fb 78%,var(--page-bottom) 100%)}
.col-1{left:30px}.col-2{left:261px}.col-3{left:498px}.col-4{left:730px}.col-5{left:964px}
.row-1{top:28px}.row-2{top:364px}
.abs{position:absolute}

/* running header */
.brand-mini{position:absolute;left:17px;top:12px;font-weight:800;font-size:9px;line-height:8.4px;color:var(--ink);letter-spacing:-.3px;text-align:center}
.header-band{position:absolute;left:67px;right:0;top:14px;height:5px;background:var(--blue-bright);
  color:#fff;font-size:3.3px;letter-spacing:.9px;line-height:5px;padding-left:11px;white-space:nowrap;font-weight:500}
.page-title{position:absolute;left:17px;top:51px;font-size:4.8px;font-weight:700;letter-spacing:.1px}
.sub-blue{position:absolute;left:17px;font-size:3.9px;font-weight:600;color:var(--blue-bright);text-decoration:underline}
.tiny{font-size:2.4px;line-height:3.2px;color:var(--muted)}

/* covers */
.cover-art{position:absolute;left:0;top:0;width:206px;height:200px}
.cover-brand{position:absolute;left:0;right:0;text-align:center;font-weight:800;font-size:24px;line-height:23px;letter-spacing:-.8px}
.cover-band{position:absolute;left:0;right:0;height:5px;text-align:center;color:#fff;font-size:3.4px;letter-spacing:1.1px;line-height:5px;font-weight:500}
.cover-title{position:absolute;left:0;right:0;text-align:center;font-weight:800;font-size:10.6px;letter-spacing:.2px}

/* letter */
.letter{position:absolute;left:17px;top:78px;width:172px;font-size:2.6px;line-height:3.25px;color:var(--muted);text-align:justify}
.letter p{margin-bottom:3.2px}

/* table of contents */
.toc{position:absolute;left:17px;top:92px;width:102px;list-style:none;font-size:3.1px;line-height:4.15px;color:var(--ink)}
.toc li{display:flex;align-items:baseline}
.toc .dots{flex:1;border-bottom:.4px dotted #777;margin:0 1px}
.toc .num{width:6px;text-align:right}

/* glossary */
.pill{position:absolute;height:10px;border-radius:5px;background:var(--blue-bright);color:#fff;font-size:2.8px;
  display:flex;align-items:center;justify-content:center;text-align:center;line-height:3px;padding:0 2px}
.gloss-text{position:absolute;width:52px;font-size:2.3px;line-height:3px;color:var(--muted);text-align:justify}

/* summaries */
.bullet{position:absolute;left:17px;font-size:2.3px;line-height:3px;color:var(--muted)}
.label{position:absolute;font-size:5.6px;font-weight:600;color:var(--muted);letter-spacing:.1px}
.bar{position:absolute;height:2.2px;background:var(--blue)}
.bar.mid{background:var(--blue-sky)}
.bar.light{background:var(--blue-pale)}
.marker{position:absolute;top:-4px;width:0;height:0;border-left:2.6px solid transparent;border-right:2.6px solid transparent;border-top:3.6px solid var(--blue);margin-left:-2.6px}
.bar.mid .marker{border-top-color:var(--blue-sky)}
.bar.light .marker{border-top-color:var(--blue-pale)}
.note{position:absolute;font-size:2.2px;line-height:2.8px;color:var(--muted)}
.section-head{position:absolute;left:17px;font-size:3.8px;font-weight:600;color:var(--blue-bright)}
.callout{position:absolute;left:17px;top:201px;width:140px;font-size:3.1px;line-height:3.8px;color:var(--blue-bright)}
</style>
</head>
<body>

<!-- Row 1 -->
<section class="page col-1 row-1">
  <svg class="cover-art" viewBox="0 0 206 200" role="img" aria-label="Photo of a glowing blue DNA double helix on a black background">
    <defs>
      <linearGradient id="dnaPhoto" x1="0" y1="0" x2="1" y2="1">
        <stop offset="0" stop-color="#0a1d3a"/><stop offset=".45" stop-color="#0b2f66"/><stop offset="1" stop-color="#03070f"/>
      </linearGradient>
    </defs>
    <path d="M0 0H206V86C160 130 70 140 0 170Z" fill="url(#dnaPhoto)"/>
    <path d="M0 170C70 140 160 130 206 86V108C160 150 70 148 0 200Z" fill="var(--blue)"/>
    <path d="M206 86V108C190 122 175 130 160 136C180 122 196 104 206 86Z" fill="#8a8d94"/>
  </svg>
  <div class="cover-brand" style="top:162px;color:var(--blue-bright)">nutrava<br>wellness</div>
  <div class="cover-band" style="top:226px;background:var(--blue-bright)">YOUR NUTRITION FOR OPTIMISED HEALTH</div>
  <div class="cover-title" style="top:279px">SAMPLE DNA REPORT</div>
</section>

<section class="page col-2 row-1">
  <div class="brand-mini">nutrava<br>wellness</div>
  <div class="header-band">YOUR NUTRITION FOR OPTIMISED HEALTH</div>
  <div class="letter">
    <p>Hi (name)!</p>
    <p>Welcome to your DNA report. Inside you will find how your genes may shape your response to caffeine, salt, sugar, fat and protein, your vitamin needs and more. Each outcome is grouped into clear sections listed in the <b>table of contents</b>, with advice for you throughout.</p>
    <p>For each outcome you will see the <b>gene and genetic variant</b> tested, <b>your result</b> and what it means for you. A short <b>glossary</b> of basic terms and links to further reading are also included.</p>
    <p>Please remember that nutrigenetics speaks in probabilities. A variant may raise your likelihood of a condition, but it does not mean you will have it. Diet, lifestyle and exercise all play an important role.</p>
    <p>In your consultation we will go through your report in detail and agree on key goals together.</p>
    <p>I hope you enjoy your report and the journey ahead!</p>
    <p>Dr. Mira Solen</p>
  </div>
</section>

<section class="page col-3 row-1">
  <div class="brand-mini">nutrava<br>wellness</div>
  <div class="header-band">YOUR NUTRITION FOR OPTIMISED HEALTH</div>
  <h2 class="page-title" style="top:78px">TABLE OF CONTENTS:</h2>
  <ul class="toc">
    <li>Glossary of Terms<span class="dots"></span><span class="num">4</span></li>
    <li>Summary of Your Results<span class="dots"></span><span class="num">5</span></li>
    <li>High Protein Diet<span class="dots"></span><span class="num">10</span></li>
    <li>Low Fat Diet<span class="dots"></span><span class="num">11</span></li>
    <li>Saturated Fat<span class="dots"></span><span class="num">12</span></li>
    <li>Meal Timing<span class="dots"></span><span class="num">13</span></li>
    <li>Physical Activity<span class="dots"></span><span class="num">14</span></li>
    <li>Cardio Training and Weight<span class="dots"></span><span class="num">15</span></li>
    <li>Exercise Motivation<span class="dots"></span><span class="num">16</span></li>
    <li>Sugar Preference<span class="dots"></span><span class="num">18</span></li>
    <li>Bitter Taster Status<span class="dots"></span><span class="num">19</span></li>
    <li>Salt Preference<span class="dots"></span><span class="num">20</span></li>
    <li>Salt Sensitivity<span class="dots"></span><span class="num">22</span></li>
    <li>Caffeine Sensitivity<span class="dots"></span><span class="num">23</span></li>
    <li>Omega-3<span class="dots"></span><span class="num">24</span></li>
    <li>Glucose Levels<span class="dots"></span><span class="num">25</span></li>
    <li>Glucose and Meal Timing<span class="dots"></span><span class="num">26</span></li>
    <li>Insulin Resistance<span class="dots"></span><span class="num">27</span></li>
    <li>Vitamin A<span class="dots"></span><span class="num">29</span></li>
    <li>Folate And Vitamin B2<span class="dots"></span><span class="num">30</span></li>
    <li>Vitamin B12<span class="dots"></span><span class="num">31</span></li>
    <li>Vitamin D<span class="dots"></span><span class="num">32</span></li>
    <li>Iron Overload<span class="dots"></span><span class="num">33</span></li>
    <li>Low Iron Status<span class="dots"></span><span class="num">34</span></li>
    <li>Choline<span class="dots"></span><span class="num">35</span></li>
    <li>Lactose Tolerance<span class="dots"></span><span class="num">37</span></li>
    <li>Gluten Sensitivity<span class="dots"></span><span class="num">38</span></li>
  </ul>
</section>

<section class="page col-4 row-1">
  <div class="brand-mini">nutrava<br>wellness</div>
  <div class="header-band">YOUR NUTRITION FOR OPTIMISED HEALTH</div>
  <h2 class="page-title" style="top:78px">GLOSSARY OF TERMS</h2>
  <div class="pill" style="left:20px;top:90px;width:53px">DNA</div>
  <div class="pill" style="left:77px;top:90px;width:53px">GENE</div>
  <div class="pill" style="left:133px;top:90px;width:53px">GENETIC VARIANT</div>
  <p class="gloss-text" style="left:21px;top:104px">DNA is a long molecule carrying your unique genetic code, built from four letters: A, T, C and G.</p>
  <p class="gloss-text" style="left:78px;top:104px">A gene is a short section of DNA holding instructions for making a specific protein in the body.</p>
  <p class="gloss-text" style="left:134px;top:104px">Everyone carries the same genes, but small differences between versions make each of us unique.</p>
  <div class="pill" style="left:20px;top:171px;width:53px">SINGLE NUCLEOTIDE POLYMORPHISM &amp; GENOTYPE</div>
  <div class="pill" style="left:77px;top:171px;width:53px">NUTRIGENETICS AND NUTRIGENOMICS</div>
  <div class="pill" style="left:133px;top:171px;width:53px">PERSONALISED NUTRITION</div>
  <p class="gloss-text" style="left:21px;top:185px">A single letter change in DNA is a variant. Two copies, one from each parent, form your genotype.</p>
  <p class="gloss-text" style="left:78px;top:185px">Nutrigenetics looks at how genes shape our response to food; nutrigenomics at how food affects our genes.</p>
  <p class="gloss-text" style="left:134px;top:185px">Advice tailored to your genes, diet, preferences, body composition and lifestyle to support optimal health.</p>
</section>

<section class="page col-5 row-1">
  <div class="brand-mini">nutrava<br>wellness</div>
  <div class="header-band">YOUR NUTRITION FOR OPTIMISED HEALTH</div>
  <h2 class="page-title" style="top:79px">SUMMARY OF YOUR RESULTS</h2>
  <div class="section-head" style="top:92px;line-height:4.4px">MACRONUTRIENT RATIO FOR<br>HEALTHY WEIGHT AND GLUCOSE LEVELS</div>
  <p class="bullet" style="top:106px">• You are a high protein and low carb responder</p>
  <p class="bullet" style="top:113px">• For healthy glucose levels, adhere to a dietary<br>&nbsp; pattern such as the Mediterranean diet</p>
  <svg class="abs" style="left:113px;top:44px" width="78" height="78" viewBox="-39 -39 78 78" role="img" aria-label="Pie chart: protein 25%, fat 35%, carbohydrate 40%">
    <g fill="#fff" stroke="var(--blue-bright)" stroke-width="2.4" stroke-linejoin="round">
      <path d="M0 0L-33 0A33 33 0 0 1 0 -33Z" transform="translate(-1.5 -1.5)"/>
      <path d="M0 0L0 -33A33 33 0 0 1 26.7 19.4Z" transform="translate(1.5 -.5)"/>
      <path d="M0 0L26.7 19.4A33 33 0 0 1 -33 0Z" transform="translate(-.5 1.5)" stroke="var(--blue-sky)"/>
    </g>
    <g font-family="Montserrat, Arial, sans-serif" font-size="2.8" font-weight="700" fill="var(--blue)" text-anchor="middle">
      <text x="-14" y="-15">Protein</text><text x="-14" y="-11.5">25%</text>
      <text x="16" y="-8">Fat</text><text x="16" y="-4.5">35%</text>
      <text x="-2" y="16">Carbohydrate</text><text x="-2" y="19.5">40%</text>
    </g>
  </svg>
  <svg class="abs" style="left:18px;top:131px" width="16" height="16" viewBox="0 0 16 16" aria-hidden="true">
    <circle cx="8" cy="8" r="6.5" fill="none" stroke="var(--blue-bright)" stroke-width="1.2"/>
    <path d="M8 4V8L10.5 9.5" fill="none" stroke="var(--blue-bright)" stroke-width="1.1" stroke-linecap="round"/>
  </svg>
  <div class="section-head" style="top:152px;text-decoration:underline">MEAL TIMING</div>
  <p class="bullet" style="top:160px">• Distribute your meals evenly throughout the day</p>
  <p class="bullet" style="top:167px">• Avoid high carb meals for breakfast and opt for meals higher in protein for early breakfast and late dinner</p>
  <svg class="abs" style="left:18px;top:182px" width="16" height="16" viewBox="0 0 16 16" aria-hidden="true">
    <g fill="none" stroke="var(--blue-bright)" stroke-width="1.4" stroke-linecap="round" stroke-linejoin="round">
      <circle cx="10.5" cy="2.6" r="1.4" fill="var(--blue-bright)" stroke="none"/>
      <path d="M9.5 5L7 9.5L10 11.5L9 15"/><path d="M9.5 5L12.5 7.5L14.5 7"/><path d="M9 5.5L5.5 6L4 8"/><path d="M7 9.5L5 13L2 13"/>
    </g>
  </svg>
  <div class="section-head" style="top:200px;text-decoration:underline">PHYSICAL ACTIVITY</div>
  <p class="bullet" style="top:208px">• Try and do more than 150 min of moderate/75 min of vigorous intensity per week</p>
  <p class="bullet" style="top:215px">• Strength building exercises on 2 days a week (e.g. yoga, pilates, weight training, body weight exercises)</p>
  <p class="callout" style="top:228px">FOCUS ON CARDIO TRAINING IF TRYING TO LOSE OR MANAGE WEIGHT, AIM FOR FREQUENT AND SHORTER SESSIONS</p>
</section>

<!-- Row 2 -->
<section class="page col-1 row-2">
  <div class="brand-mini">nutrava<br>wellness</div>
  <div class="header-band">YOUR NUTRITION FOR OPTIMISED HEALTH</div>
  <h2 class="page-title" style="top:51px">SUMMARY OF YOUR RESULTS</h2>
  <div class="sub-blue" style="top:63px">VITAMIN AND MINERAL STATUS (LEGEND)</div>
  <div class="bar" style="left:20px;top:79px;width:85px"><span class="marker" style="left:3%"></span></div>
  <p class="note" style="left:113px;top:78px">No predisposition for low levels/ typical need</p>
  <div class="bar mid" style="left:20px;top:89px;width:85px"><span class="marker" style="left:50%"></span></div>
  <p class="note" style="left:113px;top:88px">Medium predisposition for low levels/moderately higher need</p>
  <div class="bar light" style="left:20px;top:99px;width:85px"><span class="marker" style="left:96%"></span></div>
  <p class="note" style="left:113px;top:98px">High predisposition for low levels/higher need</p>

  <div class="label" style="left:19px;top:121px">VITAMIN A</div>
  <div class="bar" style="left:20px;top:133px;width:85px"><span class="marker" style="left:50%"></span></div>
  <div class="label" style="left:113px;top:121px">IRON</div>
  <div class="bar mid" style="left:113px;top:133px;width:80px"><span class="marker" style="left:96%"></span></div>

  <div class="label" style="left:19px;top:148px">FOLATE AND VITAMIN B2</div>
  <div class="bar mid" style="left:20px;top:160px;width:85px"><span class="marker" style="left:50%"></span></div>
  <div class="label" style="left:113px;top:148px">CHOLINE</div>
  <div class="bar" style="left:113px;top:160px;width:80px"><span class="marker" style="left:96%"></span></div>

  <div class="label" style="left:19px;top:175px">VITAMIN B12</div>
  <div class="bar" style="left:20px;top:187px;width:85px"><span class="marker" style="left:50%"></span></div>
  <div class="label" style="left:113px;top:175px">OMEGA-3</div>
  <div class="bar mid" style="left:113px;top:187px;width:80px"><span class="marker" style="left:50%"></span></div>

  <div class="label" style="left:19px;top:205px">VITAMIN D</div>
  <div class="bar mid" style="left:20px;top:217px;width:85px"><span class="marker" style="left:50%"></span></div>
</section>

<section class="page col-2 row-2">
  <div class="brand-mini">nutrava<br>wellness</div>
  <div class="header-band">YOUR NUTRITION FOR OPTIMISED HEALTH</div>
  <h2 class="page-title" style="top:51px">SUMMARY OF YOUR RESULTS</h2>
  <div class="sub-blue" style="top:63px">TASTE PREFERENCES</div>
  <p class="bullet" style="top:75px">• You likely have a "sweet tooth"</p>
  <p class="bullet" style="top:82px">• You are a medium taster for bitter</p>
  <p class="bullet" style="top:89px">• Your preference for salty foods is not high</p>
  <p class="bullet" style="top:96px">• Be mindful of your intake of sweet foods</p>
  <p class="bullet" style="top:103px">• Follow recommendations for salt intake<br>&nbsp; based on your salt sensitivity genotype</p>
  <svg class="abs" style="left:124px;top:40px" width="56" height="100" viewBox="0 0 56 100" role="img" aria-label="Arrow ranking taste preferences: sweet, bitter, salty">
    <defs>
      <linearGradient id="arrowFill" x1="0" y1="0" x2="0" y2="1">
        <stop offset="0" stop-color="#4a6cf0"/><stop offset=".5" stop-color="#b9c8fb"/><stop offset="1" stop-color="#ffffff" stop-opacity="0"/>
      </linearGradient>
    </defs>
    <path d="M28 2L54 26H40V98H16V26H2Z" fill="url(#arrowFill)" stroke="var(--blue)" stroke-width=".8"/>
    <g font-family="Montserrat, Arial, sans-serif" font-size="3.4" fill="var(--ink)" text-anchor="middle">
      <text x="28" y="30">SWEET</text><text x="28" y="48">BITTER</text><text x="28" y="67">SALTY</text>
    </g>
    <path d="M28 33V42M28 51V61" stroke="var(--blue)" stroke-width=".5"/>
  </svg>
  <div class="label" style="left:17px;top:123px">SALT SENSITIVITY</div>
  <div class="bar" style="left:17px;top:137px;width:81px"><span class="marker" style="left:96%"></span></div>
  <p class="note" style="left:106px;top:136px">Blood pressure is sensitive to salt. Eat no more than 4 grams per day</p>
  <div class="label" style="left:17px;top:151px">CAFFEINE SENSITIVITY</div>
  <div class="bar light" style="left:17px;top:164px;width:81px"><span class="marker" style="left:3%"></span></div>
  <p class="note" style="left:106px;top:163px">You are a fast caffeine metaboliser<br>Your maximal caffeine intake = 400 mg (3-4 cups of coffee daily)</p>
  <div class="label" style="left:17px;top:179px">LACTOSE INTOLERANCE</div>
  <div class="bar light" style="left:17px;top:192px;width:81px"><span class="marker" style="left:96%"></span></div>
  <p class="note" style="left:106px;top:191px">You may be intolerant to lactose</p>
  <div class="label" style="left:17px;top:206px">GLUTEN SENSITIVITY</div>
  <div class="bar" style="left:17px;top:220px;width:81px"><span class="marker" style="left:3%"></span></div>
  <p class="note" style="left:106px;top:219px">You are likely gluten tolerant</p>
</section>

<section class="page col-3 row-2" style="background:linear-gradient(180deg,#ffffff 55%,#ead6fb 80%,#d3aef5 100%)">
  <svg class="cover-art" viewBox="0 0 206 200" role="img" aria-label="Photo of a person measuring their waist with a tape measure beside a glowing DNA strand">
    <defs>
      <linearGradient id="weightPhoto" x1="0" y1="0" x2="1" y2="1">
        <stop offset="0" stop-color="#8a6f86"/><stop offset=".45" stop-color="#3a2a78"/><stop offset="1" stop-color="#1b1550"/>
      </linearGradient>
    </defs>
    <path d="M0 0H206V86C160 130 70 130 0 160Z" fill="url(#weightPhoto)"/>
    <path d="M0 160C70 130 160 130 206 86V108C160 150 70 150 0 195Z" fill="#b515c9"/>
    <path d="M206 86V108C190 122 175 130 160 136C180 122 196 104 206 86Z" fill="#8a8d94"/>
  </svg>
  <div class="cover-brand" style="top:157px;color:var(--magenta)">nutrava<br>wellness</div>
  <div class="cover-band" style="top:221px;background:var(--magenta)">YOUR NUTRITION FOR OPTIMISED HEALTH</div>
  <div class="cover-title" style="top:249px">WEIGHT MANAGEMENT</div>
</section>

<section class="page col-4 row-2">
  <svg class="cover-art" viewBox="0 0 206 200" role="img" aria-label="Illustration of a glowing blue human skeleton torso with a DNA helix on a blue grid">
    <defs>
      <linearGradient id="tastePhoto" x1="0" y1="0" x2="1" y2="1">
        <stop offset="0" stop-color="#1e74e8"/><stop offset=".5" stop-color="#3c9cff"/><stop offset="1" stop-color="#0c4fc6"/>
      </linearGradient>
    </defs>
    <path d="M0 0H206V80C160 125 70 125 0 160Z" fill="url(#tastePhoto)"/>
    <path d="M0 160C70 125 160 125 206 80V102C160 145 70 145 0 195Z" fill="var(--blue)"/>
    <path d="M206 80V102C190 116 175 124 160 130C180 116 196 98 206 80Z" fill="#8a8d94"/>
  </svg>
  <div class="cover-brand" style="top:157px;color:var(--blue-bright)">nutrava<br>wellness</div>
  <div class="cover-band" style="top:221px;background:var(--blue-bright)">YOUR NUTRITION FOR OPTIMISED HEALTH</div>
  <div class="cover-title" style="top:249px">TASTE PREFERENCES</div>
</section>

<section class="page col-5 row-2" style="background:linear-gradient(180deg,#ffffff 55%,#fdebd7 80%,#fbd3a6 100%)">
  <svg class="cover-art" viewBox="0 0 206 200" role="img" aria-label="Photo of a woman running outdoors beside a glowing orange DNA helix">
    <defs>
      <linearGradient id="cardioPhoto" x1="0" y1="0" x2="1" y2="1">
        <stop offset="0" stop-color="#6b4a2a"/><stop offset=".45" stop-color="#f08a1c"/><stop offset="1" stop-color="#b9400c"/>
      </linearGradient>
    </defs>
    <path d="M0 0H206V86C160 130 70 130 0 160Z" fill="url(#cardioPhoto)"/>
    <path d="M0 160C70 130 160 130 206 86V108C160 150 70 150 0 195Z" fill="#ea4f16"/>
    <path d="M206 86V108C190 122 175 130 160 136C180 122 196 104 206 86Z" fill="#8a8d94"/>
  </svg>
  <div class="cover-brand" style="top:157px;color:var(--orange)">nutrava<br>wellness</div>
  <div class="cover-band" style="top:221px;background:var(--orange)">YOUR NUTRITION FOR OPTIMISED HEALTH</div>
  <div class="cover-title" style="top:249px">CARDIOMETABOLIC HEALTH</div>
</section>

</body>
</html>
```